Halloway Crest Backers Guild business cards

Create a single-sided business card for the Halloway Crest Backers Guild based on the attached logo.
The additional data fields include Name, Title, Email, Phone, and website.
Please use the following as sample data:
Name: Dean Varrow
Title: Co-Founder / Investor
Email: deanvarrow@mailtern.net
Phone: 555-314-2706
Website: www.hcbackersguild.com

Target Market(s)

Start ups, entrepreneurs, venture capitalists

Industry/Entity Type

Investment

Contact Information for Business Card

Professional business card. Technology company.

Font styles to use
Serif
Sans Serif

Requirements
Must have
• Include the HCBG logo (attached)
• Name
• Title
• Email
• Phone
• Website
Should not have
• Cute, cartoony

```html
<!DOCTYPE html>
<html lang="en">
<head>
<meta charset="utf-8">
<title>Halloway Crest Backers Guild – Business Card</title>
<link rel="stylesheet" href="https://fonts.googleapis.com/css2?family=Open+Sans:wght@400&family=Roboto+Condensed:wght@400;600&display=swap">
<style>
  :root {
    --brand-green: #1f8a47;
    --ink: #333333;
    --paper: #ffffff;
    --backdrop: #4a4a4a;
    --tint-green: #dcede2;
    --tint-grey: #e3e3e3;
  }
  * { box-sizing: border-box; margin: 0; padding: 0; }
  html, body {
    width: 1200px; height: 1200px; overflow: hidden;
    background: var(--backdrop);
  }
  .card {
    position: absolute;
    left: 216px;
    width: 736px; height: 416px;
    overflow: hidden;
  }
  .card--front { top: 157px; background: var(--paper); }
  .card--back { top: 625px; background: var(--brand-green); }

  .brand {
    position: absolute;
    display: flex; align-items: center; gap: 18px;
    font-family: "Open Sans", sans-serif;
    font-weight: 400;
  }
  .brand__dot {
    flex: none; width: 44px; height: 44px; border-radius: 50%;
  }
  .brand__name { font-size: 28px; line-height: 1.2; }

  .card--front .brand { left: 26px; top: 44px; }
  .card--front .brand__dot { background: var(--brand-green); }
  .card--front .brand__name { color: var(--brand-green); }

  .card--back .brand {
    left: 50%; top: 50%; transform: translate(-50%, -50%);
  }
  .card--back .brand__dot { background: var(--paper); }
  .card--back .brand__name { color: var(--paper); }

  .texture {
    position: absolute; right: 0; top: 0;
    width: 330px; height: 100%;
    background: linear-gradient(135deg, var(--tint-green) 0%, rgba(227,227,227,0.9) 55%, rgba(255,255,255,0) 100%);
    opacity: 0.7;
  }

  .person {
    position: absolute; left: 27px; top: 222px;
    font-family: "Roboto Condensed", sans-serif;
  }
  .person__name {
    font-size: 31px; font-weight: 600; color: var(--brand-green);
    line-height: 1.1;
  }
  .person__title {
    font-size: 20px; color: var(--ink); margin-top: 4px;
  }
  .contact { list-style: none; margin-top: 18px; }
  .contact__item {
    display: flex; align-items: center; gap: 12px;
    font-size: 20px; color: var(--ink); height: 28px;
  }
  .contact__icon { width: 24px; height: 20px; flex: none; }
</style>
</head>
<body>

<section class="card card--front">
  <div class="brand">
    <span class="brand__dot"></span>
    <span class="brand__name">Halloway Crest<br>Backers Guild</span>
  </div>

  <div class="texture" role="img" aria-label="Soft green and grey decorative pattern area"></div>

  <div class="person">
    <h1 class="person__name">Dean Varrow</h1>
    <p class="person__title">Co-Founder / Investor</p>
    <ul class="contact">
      <li class="contact__item">
        <svg class="contact__icon" viewBox="0 0 24 20" aria-hidden="true">
          <path d="M2 7 Q12 0 22 7 L19 9 L16 7 L16 5 Q12 4 8 5 L8 7 L5 9 Z" fill="var(--brand-green)"/>
          <rect x="4" y="10" width="16" height="8" rx="2" fill="var(--brand-green)"/>
          <circle cx="12" cy="14" r="2.2" fill="#fff"/>
        </svg>
        555-314-2706
      </li>
      <li class="contact__item">
        <svg class="contact__icon" viewBox="0 0 24 20" aria-hidden="true">
          <rect x="1" y="3" width="22" height="14" fill="var(--brand-green)"/>
          <path d="M2 4 L12 12 L22 4 M2 16 L9 10 M22 16 L15 10" stroke="#fff" stroke-width="1.6" fill="none"/>
        </svg>
        deanvarrow@mailtern.net
      </li>
      <li class="contact__item">
        <svg class="contact__icon" viewBox="0 0 24 20" aria-hidden="true">
          <g fill="none" stroke="var(--brand-green)" stroke-width="1.4">
            <circle cx="12" cy="10" r="9"/>
            <ellipse cx="12" cy="10" rx="4" ry="9"/>
            <path d="M3 10 H21 M4.5 5.5 H19.5 M4.5 14.5 H19.5 M12 1 V19"/>
          </g>
        </svg>
        www.hcbackersguild.com
      </li>
    </ul>
  </div>
</section>

<section class="card card--back">
  <div class="brand">
    <span class="brand__dot"></span>
    <span class="brand__name">Halloway Crest<br>Backers Guild</span>
  </div>
</section>

</body>
</html>
```